依頼詳細
下記のチャック袋に印刷を考えております。
https://www.kumotsu-h.co.jp/shop/g/g081357-62915/
記載項目
高級志向のシンプルなデザインが希望です。
希望イメージ
シンプル 複雑
単色 カラフル
暗い 明るい
日常 高級
遊び心 厳粛
未来的 伝統的
女性的 男性的
希望する色
納品ファイル
• 高解像度JPG (.jpg)
• イラストレーター形式 (.ai)
補足説明
ペット向けオゾンについて参考サイト
https://www.blue-fern.com/media/senior/life/index04.html
商品は「歯」専門となります。
歯についた歯垢、歯石を柔らかくし除去しやすくする商品となります。
動物病院で実際に売られているので、処方箋っぽい感じのデザインでお願いします。
また、使用する色は1〜2色でお願いします。

```html
<!DOCTYPE html>
<html lang="ja">
<head>
<meta charset="utf-8">
<title>PETLA オゾンクリーン</title>
<link href="https://fonts.googleapis.com/css2?family=Noto+Sans+JP:wght@400;500;700&family=Roboto:wght@300;400&display=swap" rel="stylesheet">
<style>
  :root {
    --stripe-blue: #52bfe6;
    --accent-blue: #2fa6d8;
    --navy: #10233d;
    --ink: #141414;
    --paper: #ffffff;
  }
  * { margin: 0; padding: 0; box-sizing: border-box; }
  html, body { width: 882px; height: 1200px; overflow: hidden; background: var(--paper); }
  .package {
    position: relative;
    width: 882px;
    height: 1200px;
    background: var(--paper);
    font-family: "Noto Sans JP", sans-serif;
    color: var(--ink);
  }
  .stripe-field {
    position: absolute;
    left: 0; top: 82px;
    width: 100%; height: 905px;
    background: repeating-linear-gradient(
      to bottom,
      var(--stripe-blue) 0 13px,
      var(--paper) 13px 24px
    );
  }
  .title-panel {
    position: absolute;
    left: 62px; top: 212px;
    width: 768px; height: 300px;
    background: var(--paper);
  }
  .brand-name {
    position: absolute;
    left: 42px; top: 16px;
    font-family: "Roboto", sans-serif;
    font-weight: 400;
    font-size: 48px;
    line-height: 1;
    letter-spacing: 1px;
  }
  .product-name {
    position: absolute;
    left: 0; top: 70px;
    width: 100%;
    text-align: center;
    font-weight: 500;
    font-size: 100px;
    line-height: 1.15;
    letter-spacing: 0;
    white-space: nowrap;
  }
  .title-rule {
    position: absolute;
    left: 34px; top: 200px;
    width: 700px; height: 7px;
    background: var(--accent-blue);
  }
  .product-name-en {
    position: absolute;
    left: 0; top: 218px;
    width: 100%;
    text-align: center;
    font-family: "Roboto", sans-serif;
    font-weight: 300;
    font-size: 54px;
    line-height: 1.2;
  }
  .pet-silhouette {
    position: absolute;
    left: 268px; top: 540px;
    width: 250px; height: 322px;
  }
  .claim-band {
    position: absolute;
    left: 100px; top: 862px;
    width: 682px; height: 46px;
    background: var(--navy);
    color: var(--paper);
    font-size: 22px;
    font-weight: 500;
    line-height: 46px;
    text-align: center;
    letter-spacing: 1px;
    white-space: nowrap;
  }
  .maker-name, .count {
    position: absolute;
    top: 1010px;
    font-size: 40px;
    line-height: 50px;
    font-weight: 400;
    white-space: nowrap;
  }
  .maker-name { left: 72px; font-family: "Roboto", sans-serif; letter-spacing: 1px; }
  .count { left: 600px; font-family: "Noto Sans JP", sans-serif; letter-spacing: 2px; }
</style>
</head>
<body>
  <main class="package">
    <div class="stripe-field"></div>

    <section class="title-panel">
      <p class="brand-name">PETLA</p>
      <h1 class="product-name">オゾンクリーン</h1>
      <div class="title-rule"></div>
      <p class="product-name-en">Ozone clean</p>
    </section>

    <svg class="pet-silhouette" viewBox="0 0 250 322" role="img" aria-label="犬と猫が並んで座るシルエット">
      <rect x="0" y="0" width="250" height="322" rx="20" fill="#10233d"/>
    </svg>

    <p class="claim-band">歯についた歯垢、歯石を柔らかくし除去します。</p>

    <p class="maker-name">CLINIC BOTANICS</p>
    <p class="count">4 本入り</p>
  </main>
</body>
</html>
```